Web-Design for Electrcian Company

Our Customer is a small business electrian in Switzerland. He is looking for a fresh and innovative website design. He is well known for his extra service, and that they always go for the extra-mile! In his logo you also see that positive and fresh image the try to bring to the customer. the main colors are black, red and white.

the website structure will be:

- home
- services (with submenu for each service)
- references (with submenu for each category of services)
- about us (2 submenus: history and staff)
- links
- Contact

Target Market(s)

Architects, building owners, people from the age of 35 up...

Industry/Entity Type

Small Business

```html
<!DOCTYPE html>
<html lang="en">
<head>
<meta charset="utf-8">
<title>Brunner + Meier Elektro AG</title>
<link rel="stylesheet" href="https://fonts.googleapis.com/css2?family=Source+Sans+3:ital,wght@0,400;0,600;0,700;1,400&display=swap">
<style>
  :root {
    --red: #d6202a;
    --red-dark: #6e0808;
    --red-band: #b80505;
    --ink: #2b2b2b;
    --heading: #555555;
    --copy: #999999;
    --body: #666666;
    --footer: #2f2f28;
    --white: #ffffff;
    --gold: #e0a626;
    --pink: #f0a0a8;
    --sun: #f2b705;
  }
  * { box-sizing: border-box; margin: 0; padding: 0; }
  html, body { width: 1200px; height: 1125px; overflow: hidden; }
  body {
    position: relative;
    font-family: "Source Sans 3", "Myriad Pro", sans-serif;
    color: var(--body);
    background: linear-gradient(#d6d6d6 440px, #f2f2f2 900px, #ffffff 1072px);
  }
  .abs { position: absolute; }

  /* Header */
  .site-header {
    position: absolute; left: 0; top: 0; width: 1200px; height: 117px;
    background: linear-gradient(#ffffff, #e7e7e7);
    border-bottom: 5px solid #cfcfcf;
  }
  .brand { left: 125px; top: 6px; display: flex; align-items: center; gap: 22px; }
  .brand-dot {
    width: 100px; height: 100px; border-radius: 50%;
    border: 4px solid var(--red); background: var(--white);
  }
  .brand-name { font-size: 32px; font-weight: 600; color: var(--ink); letter-spacing: -0.3px; }
  .main-nav { left: 706px; top: 48px; display: flex; align-items: center; font-size: 14px; color: var(--heading); }
  .main-nav a { color: inherit; text-decoration: none; }
  .main-nav .current {
    width: 89px; height: 23px; line-height: 23px; text-align: center;
    background: var(--red); color: #3a0a0a; border-radius: 3px; margin-right: 22px;
  }
  .main-nav a + a { margin-left: 0; }
  .nav-services { margin-right: 25px; }
  .nav-references { margin-right: 26px; }
  .nav-about { margin-right: 22px; }

  /* Hero */
  .hero {
    position: absolute; left: 0; top: 117px; width: 1200px; height: 323px;
    background: linear-gradient(var(--red-dark), var(--red-band));
  }
  .slide-frame {
    left: 238px; top: 29px; width: 722px; height: 258px;
    background: #dfe3ee; padding: 8px;
    box-shadow: 0 4px 12px rgba(0,0,0,.35);
  }
  .slide-photo {
    position: relative; width: 100%; height: 100%;
    background: linear-gradient(90deg, #b9a6cf 0%, #a893c4 50%, #6f3fb0 52%, #9a78cf 100%);
    overflow: hidden;
  }
  .slide-rule { position: absolute; left: 0; width: 100%; height: 1px; background: rgba(255,255,255,.6); }
  .slide-kicker { position: absolute; left: 40px; top: 70px; font-size: 27px; color: #b9e3f5; letter-spacing: .3px; }
  .slide-title {
    position: absolute; left: 40px; top: 96px; font-size: 58px; font-weight: 700; color: var(--white);
    text-shadow: 0 3px 6px rgba(0,0,0,.4); letter-spacing: -0.5px;
  }
  .slide-arrow { top: 130px; }

  /* Welcome */
  .welcome { left: 133px; top: 462px; width: 912px; }
  .welcome h1 { font-size: 23px; font-weight: 400; color: var(--heading); margin: 0 0 18px 3px; }
  .welcome p {
    font-family: Arial, "Helvetica Neue", sans-serif; font-size: 13.5px; line-height: 21.5px;
    color: var(--copy); text-indent: 44px; margin-bottom: 20px;
  }
  .rule-soft { left: 340px; top: 675px; width: 570px; height: 1px; background: #dcdcdc; }

  /* Columns */
  .column-title { display: flex; align-items: center; gap: 10px; font-size: 23px; color: var(--heading); }
  .col-divider { width: 1px; background: #dadada; top: 750px; height: 218px; }
  .review { left: 133px; top: 762px; width: 280px; font-size: 14.5px; line-height: 20px; }
  .review .who { font-weight: 700; color: var(--ink); }
  .review .who span { font-weight: 400; color: var(--body); }
  .review blockquote { font-style: italic; margin: 20px 0 26px; }
  .list { list-style: none; font-size: 14.5px; line-height: 20px; }
  .list li { display: flex; gap: 12px; margin-bottom: 40px; }
  .list svg { flex: none; margin-top: 3px; }

  /* Footer */
  .site-footer {
    position: absolute; left: 0; top: 1072px; width: 1200px; height: 53px;
    background: var(--footer); color: var(--white);
  }
  .footer-brand { left: 127px; top: 6px; display: flex; align-items: center; gap: 10px; font-size: 12px; }
  .footer-dot { width: 40px; height: 40px; border-radius: 50%; border: 2px solid var(--red); }
  .footer-brand strong { font-weight: 600; font-size: 13px; }
  .rss { left: 1075px; top: 17px; display: flex; align-items: center; gap: 6px; font-size: 12px; }
</style>
</head>
<body>
  <header class="site-header">
    <div class="abs brand">
      <div class="brand-dot"></div>
      <span class="brand-name">Brunner + Meier Elektro AG</span>
    </div>
    <nav class="abs main-nav">
      <a class="current" href="#">Home</a>
      <a class="nav-services" href="#">Services</a>
      <a class="nav-references" href="#">References</a>
      <a class="nav-about" href="#">About</a>
      <a href="#">Contact</a>
    </nav>
  </header>

  <section class="hero">
    <svg class="abs slide-arrow" style="left:136px" width="30" height="52" viewBox="0 0 30 52"><path d="M26 2 L4 26 L26 50" fill="none" stroke="#5a0505" stroke-width="5"/></svg>
    <svg class="abs slide-arrow" style="left:1020px" width="30" height="52" viewBox="0 0 30 52"><path d="M4 2 L26 26 L4 50" fill="none" stroke="#5a0505" stroke-width="5"/></svg>
    <div class="abs slide-frame">
      <div class="slide-photo" role="img" aria-label="Photo of modern pendant lights in a violet-lit interior">
        <div class="slide-rule" style="top:59px"></div>
        <div class="slide-rule" style="top:161px"></div>
        <div class="slide-kicker">BRUNNER + MEIER ELEKTRO AG</div>
        <div class="slide-title">Modern Lightning</div>
      </div>
    </div>
  </section>

  <section class="abs welcome">
    <h1>Welcome to our website!</h1>
    <p>Lorem ipsum dolor sit amet, consectetur adipiscing elit. Integer lectus. Donec pharetra molestie nunc. Sed mattis, erat sit amet vehicula consectetur, purus pede consectetur quam, non tempor orci ligula ac mauris. Vestibulum lacus erat, egestas vel, posuere sit amet, molestie eget, ipsum. Cras diam nibh, placerat sit amet, dictum eget, varius a, nisi. Suspendisse ac tellus.</p>
    <p>Lorem ipsum dolor sit amet, consectetur adipiscing elit. Integer lectus. Donec pharetra molestie nunc. Sed mattis, erat sit amet vehicula consectetur, purus pede consectetur quam, non tempor orci ligula ac mauris. Vestibulum lacus erat, egestas vel, posuere sit amet, molestie eget, ipsum. Cras diam nibh, placerat sit amet, dictum eget, varius a, nisi. Suspendisse ac tellus.</p>
  </section>
  <div class="abs rule-soft"></div>

  <h2 class="abs column-title" style="left:127px;top:703px">
    <svg width="48" height="30" viewBox="0 0 48 30"><rect x="2" y="8" width="34" height="18" rx="6" fill="#e8b040"/><rect x="12" y="2" width="34" height="18" rx="6" fill="#f5cc6a"/></svg>
    Customer Review
  </h2>
  <h2 class="abs column-title" style="left:455px;top:703px">
    <svg width="30" height="30" viewBox="0 0 30 30"><circle cx="15" cy="15" r="13" fill="var(--sun)"/></svg>
    About Us
  </h2>
  <h2 class="abs column-title" style="left:807px;top:704px">
    <svg width="30" height="30" viewBox="0 0 30 30"><circle cx="15" cy="15" r="13" fill="var(--pink)"/></svg>
    Services
  </h2>

  <div class="abs col-divider" style="left:423px"></div>
  <div class="abs col-divider" style="left:784px"></div>

  <section class="abs review">
    <div class="who">Adam <span>&nbsp;says:</span></div>
    <blockquote>“Lorem ipsum dolor sit amet, consectetur adipiscing elit. Integer lectus. Donec pharetra molestie nunc.”</blockquote>
    <div class="who">&nbsp;John <span>&nbsp;says:</span></div>
    <blockquote>“Lorem ipsum dolor sit amet, consectetur adipiscing elit. Integer lectus. Donec pharetra molestie nunc.”</blockquote>
  </section>

  <ul class="abs list" style="left:460px;top:766px;width:300px">
    <li><svg width="12" height="12" viewBox="0 0 12 12"><path d="M1 6 L5 10 L11 1" fill="none" stroke="#333" stroke-width="2"/></svg>Lorem ipsum dolor sit amet, consectetur adipiscing elit. Integer lectus.</li>
    <li><svg width="12" height="12" viewBox="0 0 12 12"><path d="M1 6 L5 10 L11 1" fill="none" stroke="#333" stroke-width="2"/></svg>Lorem ipsum dolor sit amet, consectetur adipiscing elit. Integer lectus.</li>
    <li><svg width="12" height="12" viewBox="0 0 12 12"><path d="M1 6 L5 10 L11 1" fill="none" stroke="#333" stroke-width="2"/></svg>Lorem ipsum dolor sit amet, consectetur adipiscing elit. Integer lectus.</li>
    <li><svg width="12" height="12" viewBox="0 0 12 12"><path d="M1 6 L5 10 L11 1" fill="none" stroke="#333" stroke-width="2"/></svg>Lorem ipsum dolor sit amet, consectetur adipiscing elit. Integer lectus.</li>
  </ul>

  <ul class="abs list" style="left:808px;top:761px;width:300px">
    <li><svg width="22" height="20" viewBox="0 0 22 20"><rect x="2" y="4" width="16" height="5" rx="2" fill="var(--gold)"/><rect x="4" y="9" width="16" height="5" rx="2" fill="#c98d18"/><rect x="2" y="14" width="16" height="5" rx="2" fill="var(--gold)"/></svg>Lorem ipsum dolor sit amet, consectetur adipiscing elit. Integer lectus.</li>
    <li><svg width="22" height="20" viewBox="0 0 22 20"><rect x="2" y="4" width="16" height="5" rx="2" fill="var(--gold)"/><rect x="4" y="9" width="16" height="5" rx="2" fill="#c98d18"/><rect x="2" y="14" width="16" height="5" rx="2" fill="var(--gold)"/></svg>Lorem ipsum dolor sit amet, consectetur adipiscing elit. Integer lectus.</li>
    <li><svg width="22" height="20" viewBox="0 0 22 20"><rect x="2" y="4" width="16" height="5" rx="2" fill="var(--gold)"/><rect x="4" y="9" width="16" height="5" rx="2" fill="#c98d18"/><rect x="2" y="14" width="16" height="5" rx="2" fill="var(--gold)"/></svg>Lorem ipsum dolor sit amet, consectetur adipiscing elit. Integer lectus.</li>
    <li><svg width="22" height="20" viewBox="0 0 22 20"><rect x="2" y="4" width="16" height="5" rx="2" fill="var(--gold)"/><rect x="4" y="9" width="16" height="5" rx="2" fill="#c98d18"/><rect x="2" y="14" width="16" height="5" rx="2" fill="var(--gold)"/></svg>Lorem ipsum dolor sit amet, consectetur adipiscing elit. Integer lectus.</li>
  </ul>

  <footer class="site-footer">
    <div class="abs footer-brand">
      <div class="footer-dot"></div>
      <strong>Brunner + Meier Elektro AG</strong>
      <span>© 2012. All rights reserved.</span>
    </div>
    <div class="abs rss">
      <svg width="14" height="14" viewBox="0 0 14 14"><rect width="14" height="14" rx="2" fill="#f08a24"/><circle cx="3.5" cy="10.5" r="1.5" fill="#fff"/><path d="M2.5 6.5 A5 5 0 0 1 7.5 11.5 M2.5 3 A8.5 8.5 0 0 1 11 11.5" fill="none" stroke="#fff" stroke-width="1.6"/></svg>
      RSS
    </div>
  </footer>
</body>
</html>
```